Manuka honey wholesales and exports

We need business cards for our honey distribution company based in New Zealand. We supply shops locally and export Manuka honey around the world.
We deal with a very high quality and 100% natural product that can be used for medical, general health as well as food. We are looking business cards that show our honey products are of a high quality with a modern look.

Target Market(s)

Health and medical retailers and importers

Industry/Entity Type

Wholesale

Contact Information for Business Card

Tevin Apiary NZ Limited

www.tevinapiarynz.example

Derek Fawley

M +64 219036482

E tevinapiarynz@mailbox.example

PO Box 58-214
Takapuna
North Shore
Auckland
New Zealand

Font styles to use
Serif

Requirements
Must have
• (Tevin Apiary NZ Limited) with some artwork on one side and all details on the other side.
Nice to have
• I have seen a very simple card with large yellow and black stripes on one side with a company name.. looked clean and simple so something similar or just let the creative beast inside you take over and we will see what you can come up with.

```html
<!DOCTYPE html>
<html lang="en">
<head>
<meta charset="utf-8">
<title>Tevin Apiary NZ Limited – Business Card</title>
<link href="https://fonts.googleapis.com/css2?family=Playfair+Display:wght@700;900&family=Playfair+Display+SC:wght@400;700;900&display=swap" rel="stylesheet">
<style>
  :root {
    --backdrop: #c2b4b4;
    --ink: #000000;
    --charcoal: #231f20;
    --honey: #fcd800;
    --amber: #f8a81c;
    --white: #ffffff;
  }
  html, body {
    margin: 0;
    width: 1200px;
    height: 1000px;
    overflow: hidden;
    background: var(--backdrop);
  }
  .canvas {
    position: relative;
    width: 1200px;
    height: 1000px;
  }
  .card {
    position: absolute;
    left: 293px;
    width: 616px;
    height: 397px;
    overflow: hidden;
    box-shadow: 0 1px 3px rgba(0,0,0,0.35);
  }
  /* Front */
  .card--front {
    top: 72px;
    background: radial-gradient(circle at 100% 0%, #4a4a4a 0%, #1c1c1c 35%, var(--ink) 65%);
  }
  .stripe-band {
    position: absolute;
    top: 0;
    height: 100%;
    background: repeating-linear-gradient(
      -20deg,
      var(--honey) 0px,
      var(--honey) 30px,
      var(--charcoal) 30px,
      var(--charcoal) 52px
    );
  }
  .card--front .stripe-band {
    left: 151px;
    width: 139px;
    background: repeating-linear-gradient(
      -20deg,
      var(--honey) 0px,
      var(--honey) 30px,
      var(--ink) 30px,
      var(--ink) 52px
    );
  }
  .company-name {
    position: absolute;
    left: 72px;
    top: 128px;
    margin: 0;
    font-family: "Playfair Display", Georgia, serif;
    font-weight: 900;
    color: var(--white);
    line-height: 1;
    text-shadow: 0 3px 6px rgba(0,0,0,0.45);
  }
  .company-name__line {
    display: block;
    font-size: 96px;
    line-height: 84px;
    letter-spacing: -1px;
  }
  .company-name__suffix {
    display: block;
    font-size: 52px;
    line-height: 56px;
    letter-spacing: -1px;
  }
  /* Back */
  .card--back {
    top: 531px;
    background: radial-gradient(circle at 100% 0%, var(--amber) 0%, #fbc40a 35%, var(--honey) 70%);
  }
  .card--back .stripe-band {
    left: 0;
    width: 115px;
  }
  .contact {
    position: absolute;
    left: 174px;
    top: 58px;
    font-family: "Playfair Display SC", Georgia, serif;
    color: var(--charcoal);
  }
  .contact__name {
    margin: 0;
    font-size: 35px;
    font-weight: 700;
    line-height: 40px;
  }
  .contact__lines {
    margin: 2px 0 0;
    font-size: 13px;
    font-weight: 700;
    line-height: 20px;
  }
  .contact__address {
    margin: 28px 0 0;
    font-style: normal;
    font-size: 17px;
    font-weight: 700;
    line-height: 24px;
  }
  .contact__web {
    position: absolute;
    left: 174px;
    top: 336px;
    margin: 0;
    font-family: "Playfair Display SC", Georgia, serif;
    font-weight: 700;
    font-size: 24px;
    color: var(--white);
    text-shadow: 0 2px 4px rgba(0,0,0,0.35);
    text-transform: uppercase;
  }
</style>
</head>
<body>
<main class="canvas">
  <section class="card card--front" aria-label="Card front">
    <div class="stripe-band"></div>
    <h1 class="company-name">
      <span class="company-name__line">TEVIN</span>
      <span class="company-name__line">APIARY</span>
      <span class="company-name__suffix">NZ LIMITED</span>
    </h1>
  </section>

  <section class="card card--back" aria-label="Card back">
    <div class="stripe-band"></div>
    <div class="contact">
      <h2 class="contact__name">Derek Fawley</h2>
      <p class="contact__lines">M: +64 219036482<br>E: tevinapiarynz@mailbox.example</p>
      <address class="contact__address">
        PO Box 58-214<br>
        Takapuna<br>
        North Shore<br>
        Auckland<br>
        New Zealand
      </address>
    </div>
    <p class="contact__web">www.tevinapiarynz.example</p>
  </section>
</main>
</body>
</html>
```